Business Card design for Brightvale Global

we need a business card design for our company. we are a trading company based in LA.

Company Name: Brightvale Global Corp.
Contact: Marla Ostrov
Title: CEO
Tel: 310-447-2093
Email: bvgcorp7@mailnest.example

Target Market(s)

International, especially China

Industry/Entity Type

Trade

Colors
3276b5
34a7d8
0555a3
0493ce
85cae6
85acd3
d0dfed
cee9f5

Requirements
Must have
• Logo and contact, to have international/global feeling

```html
<!DOCTYPE html>
<html lang="en">
<head>
<meta charset="utf-8">
<title>Brightvale Global – Business Card</title>
<link href="https://fonts.googleapis.com/css2?family=Exo+2:wght@400;600;700&display=swap" rel="stylesheet">
<style>
  :root {
    --page-bg: #eef1f4;
    --brand-deep: #0555a3;
    --brand-mid: #0493ce;
    --brand-light: #34a7d8;
    --brand-navy: #0b2f63;
    --card-white: #ffffff;
    --text-grey: #3d3f44;
    --front-edge: #08356e;
  }
  * { margin: 0; padding: 0; box-sizing: border-box; }
  html, body {
    width: 1200px;
    height: 800px;
    overflow: hidden;
  }
  body {
    background: var(--page-bg);
    font-family: "Exo 2", sans-serif;
    display: flex;
    align-items: center;
    justify-content: center;
    gap: 40px;
  }
  .card {
    width: 520px;
    height: 297px;
    border-radius: 4px;
    box-shadow: 0 10px 28px rgba(10, 30, 60, 0.18);
    position: relative;
    overflow: hidden;
  }
  .card--front {
    background: radial-gradient(ellipse at 40% 45%, var(--brand-mid) 0%, var(--brand-deep) 45%, var(--front-edge) 100%);
    display: flex;
    align-items: center;
    justify-content: center;
  }
  .brand {
    display: flex;
    align-items: center;
    gap: 14px;
  }
  .brand__dot {
    border-radius: 50%;
    flex: none;
  }
  .brand__name {
    font-weight: 600;
    white-space: nowrap;
    letter-spacing: 0.5px;
  }
  .card--front .brand__dot {
    width: 46px;
    height: 46px;
    border: 3px solid var(--card-white);
  }
  .card--front .brand__name {
    color: var(--card-white);
    font-size: 40px;
  }
  .card--back {
    background: var(--card-white);
    display: flex;
    flex-direction: column;
    align-items: center;
    padding-top: 52px;
  }
  .card--back .brand__dot {
    width: 34px;
    height: 34px;
    background: var(--brand-light);
  }
  .card--back .brand__name {
    color: var(--brand-deep);
    font-size: 30px;
  }
  .contact {
    margin-top: 30px;
    text-align: center;
  }
  .contact__name {
    font-weight: 700;
    font-size: 20px;
    letter-spacing: 1.5px;
    color: var(--brand-navy);
    text-transform: uppercase;
  }
  .contact__title {
    font-size: 15px;
    color: var(--text-grey);
    letter-spacing: 1px;
    margin-top: 2px;
  }
  .contact__line {
    font-size: 16px;
    color: var(--text-grey);
    letter-spacing: 0.8px;
  }
  .contact__phone { margin-top: 14px; }
</style>
</head>
<body>
  <section class="card card--front" aria-label="Card front">
    <div class="brand">
      <span class="brand__dot"></span>
      <span class="brand__name">Brightvale Global</span>
    </div>
  </section>

  <section class="card card--back" aria-label="Card back">
    <div class="brand">
      <span class="brand__dot"></span>
      <span class="brand__name">Brightvale Global</span>
    </div>
    <div class="contact">
      <p class="contact__name">Marla Ostrov</p>
      <p class="contact__title">CEO</p>
      <p class="contact__line contact__phone">310-447-2093</p>
      <p class="contact__line">bvgcorp7@mailnest.example</p>
    </div>
  </section>
</body>
</html>
```